New business card, letter head, email signature and Portfolio for our Security company.

We are an Elite security company that provides a top quality manpower services to protect high rise buildings, retail and all type of properties and would like a new business card/logo look.

- We would like the spot UV design.
- Matt black (double sided).
- We would like to incorporate a royal blue colour (feel free to experiment with it).
- Feel free to try different lengths with the card to make it stand out more than a normal business card.
- We would like the logo to be an eagle eye in the background (shines when card is tilted slightly in the background, either on the front, back or both sides of the card). Image attached as an example of eye shape (colour to be either black or royal blue).
- MAVRIN OAK GUARD PATROLS PTY. LTD. and MOGP to be placed on one side of the card and on the other side of the card to have;

- Name in slightly bigger font than the position (directly on the bottom on the name).
- Mobile number
- Email address
- Website email address
- PO BOX address

Can we please have the files in a format that we can edit.

Reason: I need to consult my business partner with the designs so far and will make a decision from there.

Target Market(s)

Security Industry

Industry/Entity Type

Business

Contact Information for Business Card

- Mobile number
- Email address
- Website email address
- PO BOX address

Logo Text

MOGP and underneath the MOGP please add MAVRIN OAK GUARD PATROLS PTY. LTD.

Font styles to use
Other font styles liked:
• bold type font

Colors
0255a3
000000

Requirements
Must have
• We are an Elite security company that provides a top quality manpower services to protect high rise buildings, retail and all type of properties and would like a new business card/logo look.
• - We would like the spot UV design.
• - Matt black (double sided).
• - We would like to incorporate a royal blue colour (feel free to experiment with it).
• - Feel free to try different lengths with the card to make it stand out more than a normal business card.
• - We would like the logo to be an eagle eye in the background (shines when card is tilted slightly in the background, either on the front, back or both sides of the card). Image attached as an example of eye shape (colour to be either black or royal blue).
• - MAVRIN OAK GUARD PATROLS PTY. LTD. and MOGP to be placed on one side of the card and on the other side of the card to have;
• - Name in slightly bigger font than the position (directly on the bottom on the name).
• - Mobile number
• - Email address
• - Website email address
• - PO BOX address
• Can we please have the files in a format that we can edit.
Nice to have
• Feel free to try different lengths with the card to make it stand out more than a normal business card.
• Please find "URBAN JUNGLE" font attached and incorporate MOGP into the same style with building's inside the MOGP bold front also add MAVRIN into the bottom part of the S and follow on E - Elite on the bottom S - SECURITY on the bottom S - SERVICES on the bottom of each letter.
• other than that, I'll be happy with a bold modern font for the MOGP and MAVRIN OAK GUARD PATROLS in a bold and thinner font underneath.

```html
<!DOCTYPE html>
<html lang="en">
<head>
<meta charset="utf-8">
<title>Mavrin Oak Guard Patrols – Business Card</title>
<link href="https://fonts.googleapis.com/css2?family=Archivo+Black&family=Jost:wght@400;700&display=swap" rel="stylesheet">
<style>
  :root {
    --backdrop: #1b1b1b;
    --card: #262626;
    --card-edge: #121212;
    --spot-uv: #353535;
    --ink: #f2f2f2;
    --accent: #c9a85c;
  }
  * { margin: 0; padding: 0; box-sizing: border-box; }
  html, body {
    width: 1200px;
    height: 900px;
    overflow: hidden;
    background: var(--backdrop);
  }
  .canvas {
    width: 1200px;
    height: 900px;
    display: flex;
    align-items: center;
    justify-content: center;
    gap: 40px;
  }
  .card {
    position: relative;
    width: 540px;
    height: 330px;
    background: var(--card);
    border: 1px solid var(--card-edge);
    box-shadow: 0 10px 30px rgba(0,0,0,0.45);
    overflow: hidden;
  }

  /* Front: spot UV wordmark */
  .brand-block {
    position: absolute;
    left: 50%;
    top: 50%;
    transform: translate(-50%, -50%);
    text-align: center;
    color: var(--spot-uv);
  }
  .brand-name {
    font-family: "Archivo Black", sans-serif;
    font-size: 112px;
    line-height: 1;
    letter-spacing: -2px;
  }
  .brand-tagline {
    margin-top: 6px;
    font-family: "Archivo Black", sans-serif;
    font-size: 13px;
    letter-spacing: 1.5px;
  }

  /* Back: contact details */
  .mark {
    position: absolute;
    left: 70px;
    top: 118px;
    display: flex;
    align-items: center;
    gap: 10px;
    font-family: "Jost", sans-serif;
    font-weight: 700;
    font-size: 26px;
    color: var(--ink);
  }
  .mark-dot {
    width: 22px;
    height: 22px;
    border-radius: 50%;
    background: var(--accent);
  }
  .company-legal {
    position: absolute;
    left: 70px;
    bottom: 46px;
    font-family: "Jost", sans-serif;
    font-size: 11px;
    color: var(--ink);
  }
  .contact {
    position: absolute;
    left: 330px;
    top: 70px;
    font-family: "Jost", sans-serif;
    color: var(--ink);
  }
  .contact-name {
    font-weight: 700;
    font-size: 19px;
    line-height: 1.1;
  }
  .contact-role {
    font-size: 14px;
    line-height: 1.2;
    margin-bottom: 18px;
  }
  .contact-line {
    font-size: 14px;
    line-height: 1.3;
  }
</style>
</head>
<body>
  <main class="canvas">
    <section class="card card-front" aria-label="Card front">
      <div class="brand-block">
        <div class="brand-name">MOGP</div>
        <div class="brand-tagline">MAVRIN OAK GUARD PATROLS</div>
      </div>
    </section>

    <section class="card card-back" aria-label="Card back">
      <div class="mark">
        <span class="mark-dot"></span>
        <span>MOGP</span>
      </div>
      <p class="company-legal">Mavrin Oak Guard Patrols PTY. LTD.</p>
      <div class="contact">
        <p class="contact-name">DARREN KOLE</p>
        <p class="contact-role">DIRECTOR</p>
        <p class="contact-line">(123) 55-0198-4470</p>
        <p class="contact-line">darren@MOGP.com</p>
        <p class="contact-line">www.MOGP.com</p>
        <p class="contact-line">PO BOX 654321</p>
      </div>
    </section>
  </main>
</body>
</html>
```